Weekly Newsletter

Each week I send out a news update to the entire company updating everyone on the news and accomplishments of the week. I've been sending in an email but would like to start sending in a template that looks more professional. Either still in an email or perhaps something that can be turned into a PDF.
Each week I try to include something from each department:

• Headquarters
• MD Service
• Construction
• NOVA
• Richmond
• Hampton Roads
• Rockville
• Forestville
• Fleet
• Safety
• HR

For more info www.TrevalonPowerworks.com

Target Market(s)

Employees within the company. Might include an announcement area.

Industry/Entity Type

Electrical Power

Font styles to use
Sans Serif

Requirements
Must have
• Logo and style. awesome graphics

```html
<!DOCTYPE html>
<html lang="en">
<head>
<meta charset="utf-8">
<title>Trevalon Powerworks – Weekly Update</title>
<link href="https://fonts.googleapis.com/css2?family=Lato:wght@400;700;900&display=swap" rel="stylesheet">
<style>
:root{
  --red:#d7202b;
  --navy:#232c6e;
  --purple:#5b1f5e;
  --ink:#2b2b2b;
  --footer:#dcdcdc;
  --white:#ffffff;
}
*{box-sizing:border-box;margin:0;padding:0}
html,body{width:1200px;height:4557px;overflow:hidden;background:var(--white)}
body{position:relative;font-family:'Lato',Arial,sans-serif;color:var(--ink);font-size:20px;line-height:31px}
.hero{position:absolute;top:0;left:0;width:1200px;height:760px;overflow:hidden}
.hero-image{position:absolute;inset:0;background:linear-gradient(180deg,#7d0c1c 0%,#c8142a 40%,#e0253a 75%,#b3122a 100%)}
.hero-curve{position:absolute;left:0;top:0;width:1200px;height:760px}
.brand{position:absolute;top:48px;left:0;width:1200px;display:flex;justify-content:center;align-items:center;gap:14px}
.brand-mark{width:26px;height:26px;background:var(--white)}
.brand-name{font-weight:900;font-size:40px;line-height:48px;color:var(--white);letter-spacing:1px}
.hero-title{position:absolute;top:296px;width:1200px;text-align:center;color:var(--white);font-weight:700;font-size:46px;line-height:56px}
.hero-sub{position:absolute;top:352px;width:1200px;text-align:center;color:var(--white);font-size:31px;line-height:40px}
.item{position:absolute}
.author{color:var(--red);font-weight:700;font-size:22px;line-height:30px}
.dept{color:var(--navy);font-weight:700;font-size:24px;line-height:32px}
.bullet{position:absolute;padding-left:36px}
.bullet::before{content:"";position:absolute;left:6px;top:10px;width:11px;height:11px;border-top:3px solid var(--navy);border-right:3px solid var(--navy);transform:rotate(45deg)}
.sub{font-weight:700}
.reward{color:var(--red);font-weight:700;font-size:30px;line-height:40px}
.icon{position:absolute;border-radius:8px;background:linear-gradient(135deg,var(--navy),var(--purple) 50%,var(--red))}
.closing{font-size:21px}
.footer{position:absolute;left:0;bottom:0;width:1200px;height:82px;background:var(--footer);text-align:center;font-size:15px;line-height:82px;color:#555}
</style>
</head>
<body>

<header class="hero">
  <div class="hero-image" role="img" aria-label="Red-toned photo of a lit work site behind the greeting"></div>
  <svg class="hero-curve" viewBox="0 0 1200 760" preserveAspectRatio="none">
    <path d="M0 600 C350 720 750 600 1200 730 L1200 760 L0 760 Z" fill="#ffffff"/>
  </svg>
  <div class="brand"><span class="brand-mark"></span><span class="brand-name">Trevalon Powerworks</span></div>
  <h1 class="hero-title">Good Morning Everyone!!</h1>
  <p class="hero-sub">I hope you are enjoying your weekend. Her is a brief update for last week.</p>
</header>

<p class="item author" style="left:74px;top:712px">Carl Pettibone</p>
<h2 class="item dept" style="left:74px;top:755px">Rockville:</h2>
<p class="bullet" style="left:74px;top:806px;width:610px">This week Gerardo Valdez and Jaime Jordan continued work on the Bradmoor Rd. construction project installing Corvel Energy splice boxes, conduit, fiberglass poles, and Colonial post top fixtures. With the nice weather forecasted next week this project will be completed. They both also proceeded to set and picked up several knockdowns throughout Montgomery County.</p>
<p class="bullet" style="left:74px;top:1018px;width:610px">Paul Sterling and Mike Crandall resumed progress group re-lamping in the Gaithersburg and Olney areas. They both additionally completed all of Montgomery County's 311 calls, took care of all expedited outage calls provided by county residents, as well as installing multiple fixtures.</p>
<p class="item" style="left:74px;top:1178px">Great week gentlemen, thank you!</p>
<div class="icon" style="left:730px;top:784px;width:340px;height:370px" role="img" aria-label="Hard hat and gears icon"></div>

<h2 class="item dept" style="left:74px;top:1298px">Ronald Rusk:</h2>
<p class="item" style="left:74px;top:1342px">NOVA Office</p>
<p class="bullet" style="left:74px;top:1394px;width:1050px">I would like to express my appreciation for everybody that helped find work for everyone in NoVA. Vince Rowe and Melissa McCallum took on Terrance Mabry and Jose Serrano as helpers for Service for a couple of days. They are also allowing Nelson Arroyo to work with service until SRTA picks up again. Vince and I also had a nice discussion to determine the future of Greg, who we originally planned to use to backfill Steve Tomlin. However, through effective planning, we (mostly Vince with his critical thinking skills) came up with an effective solution to keep Greg busy on his current job and keep all other projects flowing smoothly.</p>
<p class="bullet" style="left:74px;top:1576px;width:1050px">Darnell Simms used Randall Reyes for a Traffic Call one day. Darnell and Herb Robbins have also been in communication to find work for our construction and traffic crew. Thankfully, Herb allowed us to send our construction and traffic crew to work on one of their big digging projects.</p>
<p class="bullet" style="left:74px;top:1701px;width:1050px">I know Randall is close to me and what I have to say may sound biased, but with Rick on vacation, the only other employee who has rapport with Martin Baumgart is Randall. Randall called Martin to see if we can work on the Toll Road on Thursday. Martin originally said that he would only allow work if Randall was leading it. Thankfully, Randall was able to convince Martin to let the crew work Thursday by pointing out that Steve ran a Toll Road crew before and has a lot of experience and that Walter Hernando would also be on the crew. Martin conceded and allowed work a day early.</p>
<p class="bullet" style="left:74px;top:1892px;width:1050px">Amy Gresham also provided her valuable advice and support, which helped move this process along.</p>
<p class="bullet" style="left:74px;top:1947px;width:1050px">It was truly a team effort this week to find work for our employees this week and going forward. We are trimming down to one SRTA crew for now to allow a backlog of work to build and other projects to finish. We will meet to plan personnel assignments each Thursday, thanks to Vince's wise decision. We have a good team down here.</p>

<h2 class="item dept" style="left:74px;top:2092px">Dylan Sorensen:</h2>
<p class="item" style="left:108px;top:2157px">Below are birthdays and anniversaries for this week:</p>
<p class="item sub" style="left:108px;top:2199px">Birthdays:</p>
<p class="bullet" style="left:108px;top:2242px;width:520px">Stone Stafford (August 1st)</p>
<p class="item sub" style="left:108px;top:2318px">Anniversaries:</p>
<p class="bullet" style="left:108px;top:2354px;width:560px">Christopher Fairley (August 3rd, 3 years)</p>
<div class="icon" style="left:730px;top:2086px;width:334px;height:316px" role="img" aria-label="Birthday cake icon"></div>

<p class="item reward" style="left:74px;top:2430px">Reward: $500.00</p>
<p class="item sub" style="left:74px;top:2497px">Employment Opportunities:</p>
<p class="bullet" style="left:74px;top:2558px;width:1050px">We are looking for a few Electricians and Equipment Operators for the construction department. If you refer someone to HR and we hire them you will receive $500 if they complete their 90 day probation period. Ask Dylan Sorensen for details.</p>

<h2 class="item dept" style="left:74px;top:2700px">Innovations:</h2>
<p class="bullet" style="left:74px;top:2758px;width:1050px">I have signed a contract with SafeGuard Pro https://safeguardpro.net/ They will be locking in and managing our safety program, along with risk management (WC), and DOT drivers. They have begun requesting data on our risks. Soon they will be tracking all aspects of safety. Within a few months they will be able to tell us who are the safest managers and employees.</p>
<p class="bullet" style="left:74px;top:2889px;width:1050px">Dawn Abbott and Phil Danforth are working hard on our Electronic DVIR program is up and running in NOVA, it will be implemented company wide on Monday. The great thing about this software is we are notified if drivers fake or rush an inspection.</p>
<p class="bullet" style="left:74px;top:3017px;width:1050px">Mobile Document management software is in the works and should arrive in testing form by Friday. This will streamline inspections and other document control.</p>
<p class="bullet" style="left:74px;top:3105px;width:1050px">The Evaluation of Keystone Ledger Software was extensive and exhaustive key evaluators are Sharon Maddox, Ashleigh Yates, Benally Upton, Michell Ramsey, from accounting. Larry Dalton, Diane Hartley and other demoed other modules of the software all giving the thumbs up.</p>
<p class="bullet" style="left:74px;top:3211px;width:1050px">We received our new accounting software this week. www.keystoneledger.com We have 21 team members in the system learning about the features via videos etc. The Resources tab (FAQs), Education tab (How To Videos) and My Account (My Webinars- Free Webinars) will be most helpful during your training process.</p>
<p class="bullet" style="left:74px;top:3321px;width:1050px">Keystone Ledger Software, Inc. welcomes Trevalon Powerworks, Inc. as a new user of KEYSTONE, a fully-integrated accounting software system designed specifically for the construction industry. With the use of this application, you should find yourself spending less time inputting data while producing more extensive, detailed reports that give you a real handle on your company's financial status.</p>

<h2 class="item dept" style="left:74px;top:3538px">Project News</h2>
<p class="bullet" style="left:74px;top:3585px;width:640px">Due to hard work by Amy Gresham, Richard Yates, and Ronald Chambers TPW is moving forward with the first Freshway Market store LED upgrade. We are building a retail lighting division with Ronald Chambers in the lead. Over the next few weeks we will be acquiring equipment and vehicles to support this effort.</p>
<p class="item" style="left:110px;top:3740px;width:620px">We should hear shortly if we won the Freshway Market lighting maintenance contract for nearly 120 stores in the DC, VA, MD, DE region.</p>
<div class="icon" style="left:815px;top:3551px;width:237px;height:255px" role="img" aria-label="Newspaper icon"></div>

<h2 class="item dept" style="left:74px;top:3906px">Marketing</h2>
<p class="bullet" style="left:74px;top:3956px;width:620px">Brittany Walsh has been hard at work organizing our marketing department. She sent out a few Email blasts over the past week as well as created brochures and hand outs for some of our managers. Please take and send her pictures of your jobs, she wants to let everyone know about the great work you do!!</p>
<p class="bullet" style="left:74px;top:4151px;width:620px">Send pictures and write ups to : marketing@trevalonpowerworks.com</p>
<div class="icon" style="left:775px;top:3928px;width:325px;height:261px" role="img" aria-label="Megaphone icon"></div>

<p class="item closing" style="left:100px;top:4294px">That's all for this week. Enjoy the rest of your weekend.</p>
<p class="item closing" style="left:100px;top:4345px">Thanks!</p>
<p class="item closing" style="left:100px;top:4397px">Mike</p>

<footer class="footer">© 2018 Company Name All right reserved</footer>

</body>
</html>
```